Its a flyer to a course entitled :
Ultrasound Course

Basically we teach students about the use of ultrasound for very sick patients

-I need a title in 3D
-I need an attractive design please
something extraordinary

Please if you have any ongoing project let me know Thanks

Dear Designers Was looking for something new that I did not see before, unfortunately did not find that yet! To clarify the idea, remember the T.V series 'KJ'.. so we have a sick patient like the one you have seen in the series and now we are using Ultrasound to help get the diagnosis and even it helps us in the procedures so basically will use the ultrasound to help saving those patients and give them the treatment in a short time.j

```html
<!DOCTYPE html>
<html lang="en">
<head>
<meta charset="utf-8">
<title>Emergency &amp; Critical Care Course Flyer</title>
<link rel="stylesheet" href="https://fonts.googleapis.com/css2?family=Arimo:wght@400;700&display=swap">
<style>
  :root {
    --page-bg: #ece9e4;
    --photo-dark: #2b2b2b;
    --photo-mid: #6d6d6d;
    --title-band: rgba(40, 40, 40, 0.72);
    --teal-deep: #177f9b;
    --teal-main: #1a87a2;
    --teal-low: #147590;
    --cyan-bright: #2bb6da;
    --panel-grey: #d8d8d8;
    --heading-teal: #17809d;
    --body-grey: #555555;
    --body-light: #e6f3f7;
    --white: #ffffff;
    --rule: #9fc6d2;
  }
  * { margin: 0; padding: 0; box-sizing: border-box; }
  html, body {
    width: 1000px; height: 1200px; overflow: hidden;
    background: var(--page-bg);
    font-family: "Arimo", Arial, sans-serif;
  }
  .flyer {
    position: absolute; left: 83px; top: 10px;
    width: 595px; height: 842px;
    transform: scale(1.4); transform-origin: top left;
    overflow: hidden; background: var(--teal-main);
    box-shadow: 0 4px 14px rgba(0,0,0,0.25);
  }
  .hero-photo {
    position: absolute; left: 0; top: 0; width: 595px; height: 360px;
    background: radial-gradient(ellipse at 55% 40%, #9a9a9a 0%, var(--photo-mid) 35%, var(--photo-dark) 90%);
  }
  .title-band {
    position: absolute; left: 0; top: 213px; width: 595px; height: 125px;
    background: var(--title-band);
  }
  .hero-title {
    position: absolute; left: 47px; top: 234px;
    font-weight: 700; font-size: 33px; line-height: 39px;
    color: var(--white); letter-spacing: 0.5px;
    text-shadow: 1px 1px 0 #111, 2px 2px 0 #111, 3px 3px 2px rgba(0,0,0,0.6);
  }
  .band-deep { position: absolute; left: 0; top: 360px; width: 595px; height: 33px; background: var(--teal-deep); }
  .band-bright { position: absolute; left: 0; top: 393px; width: 595px; height: 32px; background: var(--cyan-bright); }
  .intro-panel {
    position: absolute; left: 0; top: 425px; width: 420px; height: 152px;
    background: var(--panel-grey);
  }
  .info-panel {
    position: absolute; left: 0; top: 577px; width: 420px; height: 265px;
    background: linear-gradient(180deg, var(--teal-main), var(--teal-low));
  }
  .divider-strip { position: absolute; left: 420px; top: 425px; width: 6px; height: 417px; background: var(--cyan-bright); }
  .scan-image {
    position: absolute; left: 426px; top: 425px; width: 169px; height: 417px;
    background: linear-gradient(180deg, #0c0c0c 0%, #3a3a3a 12%, #6a6a6a 30%, #4a4a4a 50%, #8a8a8a 62%, #555 78%, #1a1a1a 100%);
  }
  .scan-label {
    position: absolute; left: 466px; top: 757px; width: 129px; height: 43px;
    background: rgba(23, 128, 155, 0.7);
    color: var(--white); font-weight: 700; font-size: 17px;
    line-height: 43px; padding-left: 14px;
  }
  .section { position: absolute; left: 17px; width: 393px; }
  .section h2 {
    font-weight: 700; text-align: center;
    border-bottom: 1px solid var(--rule); padding-bottom: 3px; margin-bottom: 6px;
  }
  .section p { font-size: 7.6px; line-height: 10.4px; padding: 0 12px; margin-bottom: 6px; }
  .section-intro { top: 441px; }
  .section-intro h2 { font-size: 18px; color: var(--heading-teal); }
  .section-intro p { color: var(--body-grey); }
  .section-online { top: 594px; }
  .section-online h2 { font-size: 18px; color: var(--body-light); }
  .section-online p { color: var(--body-light); }
  .section-about { top: 756px; }
  .section-about h2 { font-size: 15px; text-align: left; padding-left: 12px; color: var(--body-light); }
  .section-about p { font-weight: 700; color: var(--body-light); }
</style>
</head>
<body>
  <main class="flyer">
    <div class="hero-photo" role="img" aria-label="Blurred black and white photo of medical staff rushing a patient on a stretcher through a hospital corridor"></div>
    <div class="title-band"></div>
    <h1 class="hero-title">Emergency &amp; Critical<br>Care Course</h1>

    <div class="band-deep"></div>
    <div class="band-bright"></div>

    <section class="intro-panel"></section>
    <section class="info-panel"></section>
    <div class="divider-strip"></div>

    <div class="scan-image" role="img" aria-label="Grayscale ultrasound scan image"></div>
    <div class="scan-label">Ultrasound</div>

    <div class="section section-intro">
      <h2>Emergency &amp; Critical Care Course</h2>
      <p>is organized by the Departments of Intensive Care and Emergency Medicine of Halden University Hospital, Université de Varenne, in association with the Northern Society of Intensive Care and Emergency Medicine (NSIEM). The meeting is held every year in March. Started in 1980, this meeting has become established as one of the largest in its field, now attracting more than 6200 participants from countries worldwide.</p>
      <p>is organized by the Departments of Intensive Care and Emergency Medicine of Halden University Hospital, Université de Varenne, in association with the Northern Society of Intensive Care.</p>
    </div>

    <div class="section section-online">
      <h2>Online &amp; Onsite Ultrasound Education</h2>
      <p>is organized by the Departments of Intensive Care and Emergency Medicine of Halden University Hospital, Université de Varenne, in association with the Northern Society of Intensive Care and Emergency Medicine (NSIEM). The meeting is held every year in March. Started in 1980, this meeting has become established as one of the largest in its field, now attracting more than 6200 participants from countries worldwide.</p>
      <p>is organized by the Departments of Intensive Care and Emergency Medicine of Halden University Hospital, Université de Varenne, in association with the Northern Society of Intensive Care and Emergency Medicine (NSIEM). The meeting is held every year in March. Started in 1980, this meeting has become established as one of the largest in its field, now attracting more than 6200 participants from countries worldwide.</p>
    </div>

    <div class="section section-about">
      <h2>About us</h2>
      <p>Acute Care Dialogues in Emergency Medicine is an audio program dedicated to the intersection of Emergency Medicine and Critical Care. Keep up-to-date with insightful, penetrating commentary in this exciting and fast moving medical arena.</p>
    </div>
  </main>
</body>
</html>
```